Australian based company requires brochure design for new safety product.

New company with no Logo or branding - Let your imagination run wild.

Brontavel Pty Ltd need a brochure designed for marketing a safety product.
The idea of the brochure is to leave with Procurement departments of the health and safety industry for quick easy reference of product specifications and benefits.

Target Market(s)

Procurement teams of Health and Safety Industry. Quick easy reference points of specifications and benefits of product.

Industry/Entity Type

Marketing

Requirements
Must have
• Must have product details and specifications as per below, preferred format A4 sheet, front to back, with attached 6 photos, as well JPEG drawing attached.

With Government legislation a requirement all electrical cords be elevated a minimum of 2 meters on construction sites - THE CORVIMAX STAND was developed.
With over thirty years experience in the construction industry and safety requirements that continue to evolve we have designed and developed a lead stand that is ergonomic, portable and versatile. With no other product like it on the market.

BENEFITS
- Unique portable and easy to assemble Corvistand to fit in most tool boxes
- Non-conductive and highly visible
- Indoor and outdoor use
- Leads the way in working safely
- Complies with Government legislation
- Construction sites, Outdoor events and Camping grounds

FUNCTIONS
- Fully adjustable Telescopic Corvistand from 1.2 meters to 4.2 meters
- Spring loaded to lock between two surfaces
- Supports multiple leads, including temporary lighting and can also be used for Laser levels
- Can be screwed to a wall to elevate above floor finishes

For all enquires please contact brontavel@mailfern.example or Marisa Thorne 0491736628

```html
<!DOCTYPE html>
<html lang="en">
<head>
<meta charset="utf-8">
<title>The Corvimax Stand – Brontavel Pty Ltd</title>
<link rel="stylesheet" href="https://fonts.googleapis.com/css2?family=Archivo+Black&family=Roboto+Condensed:wght@400;700&family=Roboto:wght@400;700&display=swap">
<style>
  :root {
    --bg: #3b3b3b;
    --ink: #ffffff;
    --ribbon: #e02424;
    --ribbon-dark: #8e1212;
    --muted: #8a8a8a;
    --photo-sky: #9fb0bf;
    --photo-ground: #6c6660;
  }
  * { margin: 0; padding: 0; box-sizing: border-box; }
  html, body { width: 848px; height: 1200px; overflow: hidden; background: var(--bg); }
  .sheet { position: relative; width: 848px; height: 1200px; background: var(--bg); color: var(--ink); font-family: "Roboto Condensed", sans-serif; }

  .title {
    position: absolute; top: 92px; left: 0; width: 100%;
    text-align: center; font-family: "Archivo Black", sans-serif;
    font-size: 45px; letter-spacing: 1px; color: var(--bg);
    -webkit-text-stroke: 2px #e8e8e8; paint-order: stroke fill;
  }

  .ribbon { position: absolute; left: 36px; height: 28px; }
  .ribbon svg { position: absolute; left: 0; top: 0; }
  .ribbon span {
    position: relative; display: block; padding: 2px 0 0 22px;
    font-family: "Archivo Black", sans-serif; font-size: 16px; letter-spacing: 1.5px; color: var(--ink);
  }
  .ribbon--benefits { top: 219px; }
  .ribbon--functions { top: 574px; }

  .points { position: absolute; left: 58px; width: 370px; list-style: none; font-size: 20px; line-height: 26px; }
  .points li { position: relative; padding-left: 19px; margin-bottom: 13px; }
  .points li::before { content: ""; position: absolute; left: 0; top: 10px; width: 8px; height: 8px; border-radius: 50%; background: var(--ink); }
  .points--benefits { top: 262px; }
  .points--functions { top: 614px; }
  .points--functions li { margin-bottom: 12px; }

  .photo {
    position: absolute; width: 140px; height: 202px;
    border: 3px solid #fff; border-radius: 10px;
    box-shadow: 3px 4px 6px rgba(0,0,0,.55);
    background: linear-gradient(180deg, var(--photo-sky) 0%, #c9ccce 45%, var(--photo-ground) 100%);
  }
  .photo--a { left: 474px; top: 216px; }
  .photo--b { left: 652px; top: 216px; background: linear-gradient(180deg, #e6e5e2, #cfcdc8 80%, #8f8b86); }
  .photo--c { left: 474px; top: 441px; background: linear-gradient(180deg, #b7c3cc, #8d8880 45%, #4f4a44); }
  .photo--d { left: 652px; top: 441px; }
  .photo--e { left: 474px; top: 673px; background: linear-gradient(180deg, #c8cacc, #8f8d88 55%, #5b554f); }
  .photo--f { left: 652px; top: 673px; background: linear-gradient(180deg, #9b9892, #c5c2bc 50%, #807b74); }

  .tagline { position: absolute; top: 920px; right: 60px; font-family: "Roboto", sans-serif; font-size: 30px; color: var(--muted); word-spacing: 4px; }

  .contact { position: absolute; left: 0; width: 100%; text-align: center; font-family: "Roboto", sans-serif; }
  .contact--lead { top: 1013px; font-size: 30px; line-height: 44px; }
  .contact--call { top: 1104px; font-size: 33px; font-weight: 700; word-spacing: 2px; }
  .contact--call .gap { display: inline-block; width: 14px; }
</style>
</head>
<body>
<main class="sheet">
  <h1 class="title">THE CORVIMAX STAND</h1>

  <div class="ribbon ribbon--benefits">
    <svg width="148" height="28" viewBox="0 0 148 28" aria-hidden="true">
      <polygon points="0,0 10,0 10,6" fill="var(--ribbon-dark)"/>
      <polygon points="138,0 148,0 138,6" fill="var(--ribbon-dark)"/>
      <rect x="8" y="3" width="132" height="25" fill="var(--ribbon)"/>
    </svg>
    <span>BENEFITS</span>
  </div>
  <ul class="points points--benefits">
    <li>Unique portable and easy to assemble Corvistand to fit in most tool boxes</li>
    <li>Non-conductive and highly visible</li>
    <li>Indoor and outdoor use</li>
    <li>Leads the way in working safely</li>
    <li>Complies with Government legislation</li>
    <li>Construction sites, Outdoor events and</li>
  </ul>

  <div class="ribbon ribbon--functions">
    <svg width="150" height="28" viewBox="0 0 150 28" aria-hidden="true">
      <polygon points="0,0 10,0 10,6" fill="var(--ribbon-dark)"/>
      <polygon points="140,0 150,0 140,6" fill="var(--ribbon-dark)"/>
      <rect x="8" y="3" width="134" height="25" fill="var(--ribbon)"/>
    </svg>
    <span>FUNCTIONS</span>
  </div>
  <ul class="points points--functions">
    <li>Fully adjustable Telescopic Corvistand from 1.2 meters to 4.2 meters</li>
    <li>Spring loaded to lock between two surfaces</li>
    <li>Supports multiple leads, including temporary lighting and can also be used for Laser levels</li>
    <li>Can be screwed to a wall to elevate</li>
  </ul>

  <div class="photo photo--a" role="img" aria-label="Stand set up on a high-rise balcony with city skyline behind"></div>
  <div class="photo photo--b" role="img" aria-label="Stand fixed to a white wall holding a laser level"></div>
  <div class="photo photo--c" role="img" aria-label="Stand with a black base on a soil-covered rooftop site"></div>
  <div class="photo photo--d" role="img" aria-label="Stand wedged between slab and balcony on a tower site"></div>
  <div class="photo photo--e" role="img" aria-label="Worker in hi-vis beside the stand on a construction site"></div>
  <div class="photo photo--f" role="img" aria-label="Worker on a scaffold adjusting the stand under a ceiling"></div>

  <p class="tagline">Ergonomic &gt;&gt; Portable &gt;&gt; Versatile</p>

  <p class="contact contact--lead">For all enquires please contact<br>brontavel@mailfern.example</p>
  <p class="contact contact--call">or call<span class="gap"></span>Marisa Thorne 0491736628</p>
</main>
</body>
</html>
```